Lawn Maintenance Company needs attractive add for local newspaper

My company Halvern Lawn Works offers many lawn and yard services but I want this add to focus on one specific service we offer.
- Lawn Fertilizer and Weed Control -

This will be an add for our local newspaper, likely a 1/4 page

Some more information about this service.
Our customers generally call us when their lawn is over run with weeds or is performing poorly. Most of the time we set them up with a program and we return to their property every 4 - 5 weeks for another application. 95% of our customers return the following year for the same program. If the customer wishes we will also do a one time application

email: halvernlawnworks@mailpost.test
phone: call or text 555-814-2937

Target Market(s)

- Local small towns, populations less than 20,000
- Residential and Commercial customers with lawns
- People who are using the competitors service and aren't happy with it

Industry/Entity Type

Lawn Care

Requirements
Must have
• Must include our logo, email address and phone number
• - Logo
• - Email address and phone number (call or text)
• - Must focus on the service we want to sell (fertilizer and weed control)
Nice to have
• Some phrases or words that should be included, does not need to be word for word as long as the point is made
• - We service both Residential & Commercial properties
• - We offer professional service that can dramatically improve your lawn whether you are looking for a single application or a season long fertilizer/weed control program
• - Our lawn techs are licensed and certified applicators
Should not have
• I do not want any stock pictures of people, houses or equipment.

```html
<!DOCTYPE html>
<html lang="en">
<head>
<meta charset="utf-8">
<title>Halvern Lawn Works – Fertilizer &amp; Weed Control</title>
<link rel="stylesheet" href="https://fonts.googleapis.com/css2?family=Arimo:wght@400;700&display=swap">
<style>
  :root {
    --ink: #000000;
    --paper: #ffffff;
    --brand-green: #62b246;
    --slate-green: #4a6b5d;
    --brick: #c8625a;
    --white-text: #ffffff;
  }
  * { box-sizing: border-box; margin: 0; padding: 0; }
  html, body {
    width: 1053px;
    height: 1200px;
    overflow: hidden;
    background: var(--paper);
    font-family: "Arimo", Arial, Helvetica, sans-serif;
  }
  .ad {
    position: absolute;
    left: 48px;
    top: 48px;
    width: 957px;
    height: 1104px;
    border: 11px solid var(--ink);
    background: var(--paper);
    overflow: hidden;
  }
  .seasons-art {
    position: absolute;
    left: 133px;
    top: 21px;
    width: 669px;
    height: 192px;
    border-radius: 6px;
    background: linear-gradient(90deg, #8cc878 0%, #62b246 38%, #c8625a 66%, #e9e4e0 100%);
    opacity: 0.85;
  }
  .rule {
    position: absolute;
    left: 143px;
    width: 657px;
    height: 8px;
    border-radius: 4px;
    background: var(--ink);
  }
  .rule--ground { top: 215px; }
  .rule--base { top: 418px; }
  .brand {
    position: absolute;
    left: 0;
    right: 0;
    top: 230px;
    text-align: center;
    color: var(--brand-green);
    font-weight: 700;
    line-height: 1;
  }
  .brand-main {
    display: block;
    font-size: 130px;
    letter-spacing: 1px;
  }
  .brand-sub {
    display: block;
    font-size: 62px;
    letter-spacing: 9px;
    margin-top: 6px;
  }
  .benefits {
    position: absolute;
    left: 23px;
    top: 458px;
    width: 889px;
    height: 341px;
    background: var(--brick);
    border: 4px solid var(--slate-green);
    border-radius: 28px;
    padding: 0 16px;
    display: flex;
    flex-direction: column;
    color: var(--white-text);
    font-size: 44px;
    line-height: 1.04;
    text-align: center;
  }
  .benefit {
    flex: 1;
    display: flex;
    align-items: center;
    justify-content: center;
  }
  .benefit + .benefit { border-top: 2px solid var(--slate-green); }
  .email {
    position: absolute;
    left: 0;
    right: 0;
    top: 825px;
    text-align: center;
    color: var(--slate-green);
    font-size: 47px;
    line-height: 1;
  }
  .contact-band {
    position: absolute;
    left: 0;
    right: 0;
    top: 887px;
    height: 195px;
    background: var(--brand-green);
    text-align: center;
    color: var(--ink);
  }
  .contact-label {
    position: absolute;
    left: 0;
    right: 0;
    top: 15px;
    font-size: 56px;
    line-height: 1;
  }
  .phone {
    position: absolute;
    left: 0;
    right: 0;
    top: 62px;
    font-size: 132px;
    font-weight: 700;
    line-height: 1;
    letter-spacing: 3px;
  }
</style>
</head>
<body>
  <main class="ad">
    <div class="seasons-art" role="img" aria-label="Four trees through the seasons: spring buds, full summer canopy, autumn leaves falling, bare winter tree in snow"></div>
    <div class="rule rule--ground"></div>

    <h1 class="brand">
      <span class="brand-main">HALVERN</span>
      <span class="brand-sub">LAWN WORKS</span>
    </h1>
    <div class="rule rule--base"></div>

    <section class="benefits">
      <p class="benefit">We service both Residential &amp; Commercial<br>properties</p>
      <p class="benefit">We offer single applications or season long<br>fertilizer/weed control programs</p>
      <p class="benefit">All of our technicians are certified<br>by the Prairie Turf Board</p>
    </section>

    <p class="email">Email: halvernlawnworks@mailpost.test</p>

    <footer class="contact-band">
      <p class="contact-label">Call or Text:</p>
      <p class="phone">555-814-2937</p>
    </footer>
  </main>
</body>
</html>
```